This is for a River House on the water. We are looking for an entryway sign that will be at the end of our driveway. We named the House "The Maple Loft - Chasing the Sunset" as it is bad luck to not name a house on the water!!

The sign will be 36x24 and will be attached to Pier Posts to stay with the River theme. The Sign will be a 3D Poly Sandblasted sign so it will have some depth with lots of character.

House Name: The Maple Loft
Slogan: Catching the Blues
House #: 287

Also need a logo for all embroidery within the house.

Towels, linens, art, robes, etc. This would be the same as above but REMOVE the house # :)

Industry/Entity Type

Residential

Logo Text

The Maple Loft - "Chasing the Sunset"

Other font styles liked:
• See Photos - Something more fun

Colors

Designer to choose colors to be used in the design.

Requirements
Must have
• Must have The Maple Loft
• Must have Catching the Blues
• Must have a Blue Crab (Maryland Blue Crab Famous in these waters)
• Must have House # for exterior sign & removed for Embroidery and in-house items
Nice to have
• Colors & Style that go with the house. Photos of the house attached.
• Would be nice to have a sign that goes with the house. It almost looks like a cape cod style home. This is where you get Maryland Blue Crabs From. Yummy.
Should not have
• No Ocean, this is a river house.
• No Cartoon like Crabs. We want a real crab placed at an angle.

```html
<!DOCTYPE html>
<html lang="en">
<head>
<meta charset="utf-8">
<title>The Maple Loft – Entry Sign</title>
<link href="https://fonts.googleapis.com/css2?family=Cinzel:wght@600&family=Cormorant+Garamond:wght@600&family=Sansita:wght@900&display=swap" rel="stylesheet">
<style>
  :root {
    --page: #ffffff;
    --frame-bronze: #7b6b50;
    --frame-line: #ffffff;
    --panel: #070707;
    --cream: #ddd4c4;
    --title-edge: #3a3b36;
    --slogan: #ffffff;
    --gold: #a48d58;
    --crab-blue: #2f63c9;
    --crab-olive: #4e5a3c;
  }
  html, body {
    margin: 0;
    padding: 0;
    width: 1200px;
    height: 1200px;
    overflow: hidden;
    background: var(--page);
  }
  .sign {
    position: relative;
    width: 1200px;
    height: 1200px;
  }
  .sign-shape {
    position: absolute;
    inset: 0;
  }
  .house-number {
    position: absolute;
    top: 300px;
    left: 0;
    width: 1200px;
    text-align: center;
    font-family: "Cinzel", serif;
    font-weight: 600;
    font-size: 30px;
    letter-spacing: 1px;
    color: var(--cream);
    margin: 0;
  }
  .crab-photo {
    position: absolute;
    left: 346px;
    top: 340px;
    width: 520px;
    height: 395px;
  }
  .house-name {
    position: absolute;
    top: 692px;
    left: 0;
    width: 1200px;
    text-align: center;
    margin: 0;
    font-family: "Sansita", sans-serif;
    font-weight: 900;
    font-size: 122px;
    line-height: 1;
    color: var(--cream);
    letter-spacing: 1px;
    -webkit-text-stroke: 4px var(--title-edge);
    paint-order: stroke fill;
    text-shadow: 6px 6px 0 var(--title-edge), 8px 8px 0 var(--title-edge);
  }
  .slogan-row {
    position: absolute;
    top: 848px;
    left: 0;
    width: 1200px;
    display: flex;
    justify-content: center;
    align-items: center;
    gap: 20px;
  }
  .slogan {
    margin: 0;
    font-family: "Cormorant Garamond", serif;
    font-weight: 600;
    font-size: 58px;
    line-height: 1;
    color: var(--slogan);
    text-transform: uppercase;
    transform: scaleX(0.86);
    letter-spacing: 0;
  }
  .flourish {
    width: 140px;
    height: 28px;
    border-radius: 14px;
    background: linear-gradient(90deg, rgba(164,141,88,0.35), var(--gold), rgba(164,141,88,0.35));
  }
</style>
</head>
<body>
  <main class="sign">
    <svg class="sign-shape" width="1200" height="1200" viewBox="0 0 1200 1200" aria-hidden="true">
      <path class="frame-outer" d="M98 485 Q98 443 140 443 L200 443 C310 443 410 275 600 275 C790 275 890 443 1000 443 L1060 443 Q1102 443 1102 485 L1102 885 Q1102 927 1060 927 L140 927 Q98 927 98 885 Z"
        fill="none" stroke="var(--frame-bronze)" stroke-width="52" stroke-linejoin="round"/>
      <path class="frame-line" d="M98 485 Q98 443 140 443 L200 443 C310 443 410 275 600 275 C790 275 890 443 1000 443 L1060 443 Q1102 443 1102 485 L1102 885 Q1102 927 1060 927 L140 927 Q98 927 98 885 Z"
        fill="none" stroke="var(--frame-line)" stroke-width="14" stroke-linejoin="round"/>
      <path class="panel" d="M98 485 Q98 443 140 443 L200 443 C310 443 410 275 600 275 C790 275 890 443 1000 443 L1060 443 Q1102 443 1102 485 L1102 885 Q1102 927 1060 927 L140 927 Q98 927 98 885 Z"
        fill="var(--panel)"/>
    </svg>

    <p class="house-number">House #: 287</p>

    <svg class="crab-photo" viewBox="0 0 520 395" role="img" aria-label="Photograph of a Maryland blue crab, claws raised, viewed from above">
      <defs>
        <radialGradient id="crabTone" cx="50%" cy="62%" r="60%">
          <stop offset="0%" stop-color="var(--crab-olive)"/>
          <stop offset="55%" stop-color="#35507a"/>
          <stop offset="100%" stop-color="var(--crab-blue)" stop-opacity="0"/>
        </radialGradient>
      </defs>
      <ellipse cx="260" cy="220" rx="260" ry="175" fill="url(#crabTone)"/>
    </svg>

    <h1 class="house-name">The Maple Loft</h1>

    <div class="slogan-row">
      <span class="flourish" role="img" aria-label="Gold scroll flourish"></span>
      <p class="slogan">Catching the Blues</p>
      <span class="flourish" role="img" aria-label="Gold scroll flourish"></span>
    </div>
  </main>
</body>
</html>
```